Halbrook & Company

We are a boutique commercial real estate firm. For our Business card design - sleek, modern, yet high-end/classy. Please see our website: halbrookandcompany.example for details.

We currently need 2 business card names and the ability to add/change the business card information -
Name, Title, Address, Office #, Mobile #, Fax, Email and company website.

Industry/Entity Type

Real Estate

Contact Information for Business Card

Business card design - sleek, modern, yet high-end/classy. Please see our website: halbrookandcompany.example for details.

Also, we'd like to have our slogan "Precision Shapes Every Deal." somewhere in there. We'd like to make some part of it raised or a different texture if possible.
Color #'s:
blue 19 36 128
light gray 222 222 221
dark gray 107 120 128

Also, we'd like to have our slogan "Precision Shapes Every Deal." somewhere in there. We'd like to make some part of it raised or a different texture if possible - grey on one side and blue on the other - rounded edges preferred. Maybe either metal/silver/grey raised logo on the back. Thank you!!

Requirements
Must have
• Sleek, modern, clean and classy design

```html
<!DOCTYPE html>
<html lang="en">
<head>
<meta charset="UTF-8">
<title>Halbrook &amp; Company – Business Card</title>
<link href="https://fonts.googleapis.com/css2?family=Open+Sans:wght@400;600;700&display=swap" rel="stylesheet">
<style>
  :root {
    --brand-blue: #1d3fa6;
    --brand-blue-light: #3560c8;
    --brand-blue-dark: #132480;
    --text-blue: #2546a8;
    --dark-gray: #6b7880;
    --light-gray: #dededd;
    --page-bg: #e9eaec;
    --white: #ffffff;
  }
  * { margin: 0; padding: 0; box-sizing: border-box; }
  html, body {
    width: 1200px;
    height: 900px;
    overflow: hidden;
    background: var(--page-bg);
    font-family: "Open Sans", Arial, sans-serif;
  }
  .canvas {
    width: 1200px;
    height: 900px;
    display: flex;
    flex-direction: column;
    align-items: center;
    justify-content: center;
    gap: 56px;
  }
  .card {
    width: 640px;
    height: 366px;
    border-radius: 14px;
    position: relative;
    overflow: hidden;
    box-shadow: 0 8px 24px rgba(0,0,0,0.14);
  }

  /* Front (blue side) */
  .card-front {
    background: linear-gradient(135deg, var(--brand-blue-dark) 0%, var(--brand-blue) 45%, var(--brand-blue-light) 100%);
  }
  .front-logo {
    position: absolute;
    top: 52px;
    right: 48px;
    display: flex;
    align-items: center;
    gap: 14px;
  }
  .front-logo .logo-square {
    width: 34px;
    height: 34px;
    background: var(--light-gray);
  }
  .front-logo .logo-name {
    color: var(--white);
    font-weight: 700;
    font-size: 30px;
    letter-spacing: 0.5px;
    white-space: nowrap;
  }
  .slogan {
    position: absolute;
    right: 48px;
    bottom: 44px;
    color: var(--white);
    font-weight: 700;
    font-size: 17px;
    letter-spacing: 1px;
    text-transform: uppercase;
    white-space: nowrap;
  }

  /* Back (white side) */
  .card-back {
    background: var(--white);
    display: flex;
    align-items: center;
    padding: 0 40px;
  }
  .back-logo {
    display: flex;
    align-items: center;
    gap: 12px;
    width: 250px;
  }
  .back-logo .logo-square {
    width: 26px;
    height: 26px;
    background: var(--text-blue);
    flex-shrink: 0;
  }
  .back-logo .logo-name {
    color: var(--text-blue);
    font-weight: 700;
    font-size: 20px;
    white-space: nowrap;
  }
  .divider {
    width: 3px;
    height: 176px;
    background: var(--text-blue);
    margin: 0 26px 0 14px;
    flex-shrink: 0;
  }
  .contact {
    flex: 1;
  }
  .contact .person-name {
    color: var(--dark-gray);
    font-weight: 700;
    font-size: 24px;
    letter-spacing: 0.5px;
  }
  .contact .person-title {
    color: var(--text-blue);
    font-size: 18px;
    margin-bottom: 14px;
  }
  .contact-list {
    list-style: none;
  }
  .contact-list li {
    display: flex;
    align-items: flex-start;
    gap: 12px;
    color: var(--text-blue);
    font-size: 17px;
    line-height: 1.5;
    white-space: nowrap;
  }
  .contact-list svg {
    width: 16px;
    height: 16px;
    margin-top: 5px;
    flex-shrink: 0;
    fill: var(--dark-gray);
  }
</style>
</head>
<body>
<main class="canvas">

  <section class="card card-front" aria-label="Card front">
    <div class="front-logo">
      <span class="logo-square"></span>
      <span class="logo-name">Halbrook &amp; Company</span>
    </div>
    <p class="slogan">Precision Shapes Every Deal</p>
  </section>

  <section class="card card-back" aria-label="Card back">
    <div class="back-logo">
      <span class="logo-square"></span>
      <span class="logo-name">Halbrook &amp; Company</span>
    </div>
    <div class="divider"></div>
    <div class="contact">
      <p class="person-name">YOUR NAME</p>
      <p class="person-title">Your Title</p>
      <ul class="contact-list">
        <li>
          <svg viewBox="0 0 24 24" aria-hidden="true"><path d="M6.6 10.8a15.1 15.1 0 0 0 6.6 6.6l2.2-2.2c.3-.3.7-.4 1-.2 1.1.4 2.3.6 3.6.6.6 0 1 .4 1 1V20c0 .6-.4 1-1 1A17 17 0 0 1 3 4c0-.6.4-1 1-1h3.5c.6 0 1 .4 1 1 0 1.3.2 2.5.6 3.6.1.3 0 .7-.2 1z"/></svg>
          <span>123-456-2100</span>
        </li>
        <li>
          <svg viewBox="0 0 24 24" aria-hidden="true"><path d="M2 5h20v14H2zm2 2v.4l8 5 8-5V7zm0 2.8V17h16V9.8l-8 5z"/></svg>
          <span>youremail@mail.example</span>
        </li>
        <li>
          <svg viewBox="0 0 24 24" aria-hidden="true"><path d="M12 2a10 10 0 1 0 0 20 10 10 0 0 0 0-20zm0 2c1 0 2.3 2 2.8 5H9.2C9.7 6 11 4 12 4zM4.3 11h2.8c0-1.1.1-2.1.3-3H5.2a8 8 0 0 0-.9 3zm0 2a8 8 0 0 0 .9 3h2.2c-.2-.9-.3-1.9-.3-3zm4.9 0c.1 1.1.2 2.1.5 3h4.6c.3-.9.4-1.9.5-3zm0-2h5.6c-.1-1.1-.2-2.1-.5-3H9.7c-.3.9-.4 1.9-.5 3zm7.7 0h2.8a8 8 0 0 0-.9-3h-2.2c.2.9.3 1.9.3 3zm0 2c0 1.1-.1 2.1-.3 3h2.2a8 8 0 0 0 .9-3zM12 20c-1 0-2.3-1.5-2.8-2h5.6c-.5.5-1.8 2-2.8 2z"/></svg>
          <span>www.yourwebsite.example</span>
        </li>
        <li>
          <svg viewBox="0 0 24 24" aria-hidden="true"><path d="M12 2a7 7 0 0 0-7 7c0 5 7 13 7 13s7-8 7-13a7 7 0 0 0-7-7zm0 9.5A2.5 2.5 0 1 1 12 6.5a2.5 2.5 0 0 1 0 5z"/></svg>
          <span>Your address, city<br>state, ZIP 0000</span>
        </li>
      </ul>
    </div>
  </section>

</main>
</body>
</html>
```